Meridale Family Law Firm Website Renovation

We need a website redesign in SquareSpace that is more modern, user friendly, on brand, less cluttered, easier to navigate, conveys clearly what our services are, and has clear, visible calls to action.

We would like to hire and work with the winning designer to complete the remaining pages of the site.

Target Market(s)

Couples looking for divorce representation or mediation who have a conscious, progressive mindset. They are self-aware and personal development plays an important role in their lives. They want an amicable interaction and aspire to have a healthy relationship after divorce.

Age range: 30-60
Income 100K+ household

Industry/Entity Type

Family Law

Font styles to use
Sans Serif

Colors
85acd3
33a6d7
50c0af
a0cd3a

Requirements
Must have
• Please see attached doc for full creative brief details.

"Changing the way people divorce" on top of site.
Images that show happy clients and that represent males and females. Diversity inclusion is also be important.
We are looking for warm, welcoming design and imagery.
Should not have
• Not heavily attorney focused.
Please see attached brief for full description.

```html
<!DOCTYPE html>
<html lang="en">
<head>
<meta charset="utf-8">
<title>Meridale Family Law &amp; Mediation</title>
<link href="https://fonts.googleapis.com/css2?family=Quicksand:wght@400;500;700&family=Montserrat:wght@400;600;700&family=Courier+Prime&display=swap" rel="stylesheet">
<style>
:root{
  --sky:#85acd3;
  --blue:#33a6d7;
  --teal:#50c0af;
  --lime:#a0cd3a;
  --orange:#ef7a3c;
  --ink:#2f2f2f;
  --muted:#6f6f6f;
  --line:#ececec;
  --footer:#8eaedb;
  --device:#dcdcdc;
}
*{box-sizing:border-box;margin:0;padding:0}
html,body{width:1200px;height:3579px;overflow:hidden;background:#fff}
body{position:relative;font-family:'Montserrat',sans-serif;color:var(--ink)}
.abs{position:absolute}
.heading{font-family:'Quicksand',sans-serif;font-weight:400;letter-spacing:2px;color:var(--ink)}
.btn{position:absolute;display:flex;align-items:center;justify-content:center;background:var(--blue);color:#fff;font-size:12px;font-weight:700;letter-spacing:.3px;text-transform:uppercase}
.rule{position:absolute;left:0;width:1200px;height:1px;background:var(--line)}

/* header */
.brand{left:150px;top:22px;width:135px;text-align:center}
.brand-mark{width:60px;height:60px;border-radius:50%;background:var(--teal);margin:0 auto 10px}
.brand-name{font-family:'Montserrat',sans-serif;font-size:12px;letter-spacing:2.5px;color:#333;line-height:1.3}
.call{right:149px;top:40px;text-align:right;font-size:12px;color:#666}
.call strong{display:block;font-family:'Quicksand',sans-serif;font-weight:500;font-size:23px;color:var(--blue);margin-top:2px}
.nav{right:149px;top:93px;display:flex;gap:8px;font-size:12px;color:#333}
.nav span.dot{color:#999}
.nav .active{color:var(--blue);position:relative}
.nav .active:after{content:"";position:absolute;left:52px;top:26px;width:52px;height:1px;background:var(--blue)}

/* hero */
.hero{left:0;top:148px;width:1200px;height:459px;background:linear-gradient(100deg,#7c9bbd 0%,#93b3cf 45%,#86a7c9 100%)}
.hero-title{left:150px;top:238px;font-family:'Quicksand',sans-serif;font-weight:700;font-size:54px;letter-spacing:5px;color:#fff}
.hero-sub{left:150px;top:313px;width:520px;font-size:19px;line-height:36px;color:#fff}
.qualify{left:765px;top:190px;width:285px;height:378px;background:#fff;padding:20px 14px;font-size:10px;color:#444}
.qualify h3{font-family:'Montserrat',sans-serif;font-weight:400;font-size:14px;text-align:center;margin-bottom:22px}
.q{margin-bottom:6px;line-height:1.3}
.opts{display:flex;gap:18px;margin-bottom:24px;align-items:center}
.opts i{display:inline-block;width:10px;height:10px;border:1px solid #888;border-radius:50%;vertical-align:-2px;margin-right:5px}
.opts i.on{border:3px solid var(--blue)}
.field{height:26px;border:1px solid #ddd;padding:0 7px;display:flex;align-items:center;color:#666;margin-bottom:15px;font-size:10px}
.row{display:flex;gap:12px}
.row .field{flex:1}

/* unique */
.tile{width:220px;height:152px;border:1px solid var(--blue)}
.caption{width:290px;text-align:center;font-family:'Quicksand',sans-serif;font-size:14px;line-height:23px;letter-spacing:1px;color:#555}

/* two columns */
.col{width:382px;font-family:'Quicksand',sans-serif;font-size:11.5px;line-height:22.5px;letter-spacing:.8px;color:#666;text-align:justify}
.col b{color:#222;font-weight:700}

/* band */
.band{left:0;top:1491px;width:1200px;height:168px;background:var(--teal)}
.band h2{position:absolute;left:186px;top:32px;font-size:27px;font-weight:700;color:#2d2d2d}
.band p{position:absolute;left:188px;top:78px;width:385px;font-size:12px;line-height:16px;letter-spacing:.6px;color:#fff}
.band .cta{left:673px;top:66px;width:270px;height:36px;background:var(--orange);font-size:14px}

/* device frames */
.device{width:430px;height:300px;background:var(--device);border-radius:16px}
.screen{position:absolute;left:37px;top:16px;width:355px;height:268px}
.shadow{position:absolute;left:0;bottom:-35px;width:440px;height:16px;border-radius:50%;background:radial-gradient(#bdbdbd,transparent 70%)}
.play{position:absolute;left:50%;top:50%;width:50px;height:50px;margin:-25px;border-radius:50%;background:var(--blue)}
.play:after{content:"";position:absolute;left:20px;top:14px;border-left:16px solid #fff;border-top:11px solid transparent;border-bottom:11px solid transparent}
.bar{position:absolute;left:0;bottom:0;width:100%;height:30px;background:#2a2e38}
.body-text{font-family:'Quicksand',sans-serif;font-size:13px;line-height:23px;letter-spacing:.9px;color:#666}

/* reviews */
.quote{left:255px;top:2235px;width:690px;text-align:center;font-family:'Courier Prime',monospace;font-size:14.5px;line-height:22.5px;color:#666}
.stars{left:540px;top:2372px;font-size:20px;color:#c0101a;letter-spacing:6px}
.who{left:400px;top:2410px;width:400px;text-align:center;font-family:'Courier Prime',monospace;font-style:italic;font-size:11px;color:#777}

/* footer */
.footer{left:0;top:3316px;width:1200px;height:263px;background:var(--footer);color:#fff;font-size:10px;line-height:18px}
.social{display:flex;gap:17px}
.social i{display:block;width:44px;height:44px;border-radius:50%;background:#111}
</style>
</head>
<body>

<header>
  <div class="abs brand">
    <div class="brand-mark"></div>
    <div class="brand-name">MERIDALE<br>FAMILY LAW</div>
  </div>
  <div class="abs call">Call For A Free Consultation<strong>(415) 555-0172</strong></div>
  <nav class="abs nav">
    <span class="active">Home</span><span class="dot">·</span>
    <span>Our Services</span><span class="dot">·</span>
    <span>Testimonials</span><span class="dot">·</span>
    <span>Schedule / Contact</span><span class="dot">·</span>
    <span>About Us</span><span class="dot">·</span>
    <span>FAQ</span><span class="dot">·</span>
    <span>Resources</span>
  </nav>
</header>

<section class="abs hero" role="img" aria-label="Photo of a smiling mother carrying her child through a sunlit orchard, tinted blue"></section>
<h1 class="abs hero-title">Meridale Family</h1>
<p class="abs hero-sub">Efficient and positive family legal transitions without costly, painful legal battles.</p>
<div class="btn" style="left:150px;top:470px;width:224px;height:37px">Request a free consultation</div>

<form class="abs qualify">
  <h3>Do you qualify?</h3>
  <p class="q">Do you know the location of your spouse?</p>
  <div class="opts"><span><i class="on"></i>Yes</span><span><i></i>No</span></div>
  <p class="q">Can you and your spouse agree to the division of property, assets and all child related issues?</p>
  <div class="opts" style="margin-bottom:12px"><span><i class="on"></i>Yes</span><span><i></i>No</span></div>
  <div class="field" style="justify-content:space-between">Choose your state <span>▾</span></div>
  <div class="row"><div class="field">First Name</div><div class="field">Last Name</div></div>
  <div class="field">Enter your email</div>
  <div class="btn" style="position:relative;height:36px;margin-top:13px">Free eligibility check</div>
</form>

<h2 class="abs heading" style="left:0;width:1200px;top:684px;text-align:center;font-size:29px">What Makes Us Unique</h2>
<div class="abs tile" style="left:171px;top:776px;background:linear-gradient(135deg,#f3ede4,#c9a56a)" role="img" aria-label="Illustration of scales of justice and a gavel on law books"></div>
<div class="abs tile" style="left:486px;top:776px;background:linear-gradient(135deg,#eef5fb,#6fb3e0)" role="img" aria-label="Illustration of people balancing on a large scale"></div>
<div class="abs tile" style="left:803px;top:776px;background:linear-gradient(135deg,#f2f5fa,#a9c2e2)" role="img" aria-label="Illustration of documents, a pen and a small scale"></div>
<p class="abs caption" style="left:136px;top:948px">Helping families and individuals<br>to navigate the divorce transition</p>
<p class="abs caption" style="left:450px;top:948px">Minimizing cost, pain, time,<br>and collateral damage to children</p>
<p class="abs caption" style="left:768px;top:948px">Producing outcomes and result<br>in healthy co-parenting families<br>post-divorce</p>
<div class="btn" style="left:487px;top:1030px;width:225px;height:36px">Learn more</div>

<div class="rule" style="top:1112px"></div>

<h2 class="abs heading" style="left:185px;width:382px;top:1152px;text-align:center;font-size:29px">Work Together</h2>
<h2 class="abs heading" style="left:634px;width:382px;top:1152px;text-align:center;font-size:29px">Help Just For You</h2>
<p class="abs col" style="left:185px;top:1215px">Mediation is possible when both spouses are willing to negotiate their divorce agreements in good faith, with the help of a neutral mediator. Meridale Family attorney-mediators are experienced family lawyers and are skilled at helping clients <b>reach fair, workable agreements, without the cost and damage of the conventional divorce process.</b></p>
<p class="abs col" style="left:634px;top:1215px">If mediation is not possible, you need a lawyer to advise, negotiate, and possibly advocate for you. Our experienced Meridale Family lawyers offer <b>clear, confident, and highly effective advice and representation</b> while attempting to minimize financial and emotional costs to you and your family.</p>
<div class="btn" style="left:264px;top:1401px;width:225px;height:36px">Learn more</div>
<div class="btn" style="left:713px;top:1401px;width:225px;height:36px">Learn more</div>

<section class="abs band">
  <h2>Mediation or Lawyer?</h2>
  <p>Our simple, free questionnaire can help you determine if you and your spouse are suited for mediation, or if you may want legal representation for yourself.</p>
  <div class="btn cta">Take our free questionnaire</div>
</section>

<div class="abs device" style="left:150px;top:1724px">
  <div class="screen" style="background:linear-gradient(#3b3f48,#5d6a7d)" role="img" aria-label="Introductory video about a new approach to divorce">
    <div class="play"></div><div class="bar"></div>
  </div>
  <div class="shadow"></div>
</div>
<h2 class="abs heading" style="left:663px;top:1806px;font-size:29px">Who we are</h2>
<p class="abs body-text" style="left:663px;top:1858px;width:395px">Our simple, free questionnaire can help you determine if you and your spouse are suited for mediation, or if you may want legal representation for yourself.</p>

<div class="rule" style="top:2118px"></div>

<h2 class="abs heading" style="left:0;width:1200px;top:2156px;text-align:center;font-size:34px">Our Client Reviews</h2>
<svg class="abs" style="left:186px;top:2318px" width="14" height="28"><path d="M12 2 2 14l10 12" fill="none" stroke="#444" stroke-width="1.5"/></svg>
<svg class="abs" style="left:998px;top:2318px" width="14" height="28"><path d="M2 2l10 12L2 26" fill="none" stroke="#444" stroke-width="1.5"/></svg>
<p class="abs quote">“I am so grateful for my experience with Meridale Family Law &amp; Mediation. I learned so much about myself and my capacity to love, grieve, and heal. You were so great at facilitating our difficult conversations, helping both of us feel validated, and coaching us on how to work well with each other moving forward in our new co-parenting relationship.”</p>
<div class="abs stars">★★★★★</div>
<p class="abs who">Divorce Mediation Client</p>
<div class="btn" style="left:487px;top:2459px;width:225px;height:36px">Read more testimonial</div>

<div class="rule" style="top:2540px"></div>

<h2 class="abs heading" style="left:150px;top:2656px;width:400px;font-size:29px;line-height:38px">Avoiding harm to children<br>in divorce</h2>
<p class="abs body-text" style="left:150px;top:2757px;width:385px">Lorem ipsum dolor sit amet, consectetur adipisicing elit, sed do eiusmod tempor incididunt ut labore et dolore magna aliqua.</p>
<div class="abs device" style="left:620px;top:2588px">
  <div class="screen" style="background:linear-gradient(90deg,#151618 0%,#4a4a52 45%,#3d3f46 100%)" role="img" aria-label="Video of an attorney speaking to camera">
    <div class="play"></div><div class="bar"></div>
  </div>
  <div class="shadow"></div>
</div>

<div class="rule" style="top:2975px"></div>

<h2 class="abs heading" style="left:148px;top:3012px;font-size:29px">Rated by</h2>
<div class="abs" style="left:187px;top:3080px;width:166px;height:137px;border-radius:6px;background:#1f6fae" role="img" aria-label="Peer rating badge"></div>
<div class="abs" style="left:415px;top:3090px;width:215px;height:115px;border-radius:8px;background:#f4c21f" role="img" aria-label="Children's advocacy partner badge"></div>
<div class="abs" style="left:698px;top:3090px;width:90px;height:115px;border-radius:50%;background:#d9a62a" role="img" aria-label="Award medal badge"></div>
<div class="abs" style="left:848px;top:3088px;width:165px;height:120px;border-radius:50%;background:#5b3aa3" role="img" aria-label="Local recommendation badge"></div>

<footer class="abs footer">
  <p class="abs" style="left:151px;top:10px">Meridale Family Law &amp; Mediation LLC<br>1420 Aster Lane, Suite 2<br>Elmwood, Colorado 80599</p>
  <p class="abs" style="left:151px;top:100px">1+ (303) 555-0148<br>info@meridalefamilylaw.com</p>
  <p class="abs" style="left:151px;top:167px;font-weight:700">Press information</p>
  <p class="abs" style="left:151px;top:205px;font-size:9px">Website content copyright 2014-2020 Meridale Family Law &amp; Mediation LLC</p>
  <div class="abs social" style="right:150px;top:10px"><i></i><i></i><i></i></div>
  <p class="abs" style="right:150px;top:78px;font-size:12px;font-weight:600;letter-spacing:.5px">We are proud to serve your family.</p>
  <p class="abs" style="right:150px;top:130px;width:360px;text-align:right">Meridale Family Law &amp; Mediation LLC currently serves the legal needs of Colorado residents (including same-sex and other alternative families) in Elmwood County, Ashford County, Linden County, Carrow County, Halden County, Pinefield County, and Rowan County.</p>
</footer>

</body>
</html>
```